Custom t-shirts and merchandise orders t shirts and merchendise

I'd like to build a webpage to promote clothing apparel merchandise and also print on demand. A copy of my logo is attached! An example webpage for the print on demand would be pelwintops.com, Harbeckwear.com, and quillmarkpress.com. If possible, I'd like the web page colors to match the attached logo but it is not absolutely necessary.

Target Market(s)

Clipzor, Palmnest, and wendro viewers age 20-35

Industry/Entity Type

Apparel Store

Logo Text

TideRolls

Coding

Coded - Design and coding required

Number of Pages Required

5+ page

Font styles to use
Sans Serif

Requirements
Must have
• Print on demand page to custom build a shirt design.
Nice to have
• Subscribe option

```html
<!DOCTYPE html>
<html lang="en">
<head>
<meta charset="utf-8">
<title>TideRolls – Custom Tshirts</title>
<link href="https://fonts.googleapis.com/css2?family=Montserrat:wght@500;600;700;800;900&family=Roboto:wght@400;500&display=swap" rel="stylesheet">
<style>
:root{
  --ink:#111111;
  --text:#333333;
  --muted:#555555;
  --yellow:#fcbf10;
  --blue:#1a9be8;
  --blue-light:#cfe9fb;
  --band:#f4f1f2;
  --line:#cfcfcf;
  --white:#ffffff;
  --star:#f5a800;
}
*{box-sizing:border-box;margin:0;padding:0}
html,body{width:1200px;height:2827px;overflow:hidden;background:var(--white)}
body{position:relative;font-family:"Roboto",sans-serif;color:var(--text)}
.abs{position:absolute}
.brand{display:flex;align-items:center;gap:10px;font-family:"Montserrat",sans-serif;font-weight:800;color:var(--ink)}
.brand-dot{width:22px;height:22px;border-radius:50%;background:var(--blue)}
/* header */
.site-header .brand{left:130px;top:54px;font-size:32px}
.help{left:585px;top:28px;display:flex;gap:10px;align-items:center;font-family:"Montserrat",sans-serif}
.help small{display:block;font-size:12px;font-weight:600;color:var(--ink)}
.help strong{font-size:18px;font-weight:600;color:var(--ink)}
.search{left:779px;top:27px;width:174px;height:36px;border:1px solid #bbb;background:#f6f6f6;font-size:10px;font-family:"Montserrat",sans-serif;padding:11px 12px;color:#444}
.search svg{position:absolute;right:10px;top:11px}
.cart{left:973px;top:27px;width:95px;height:36px;border:1px solid #888;font-size:10px;font-family:"Montserrat",sans-serif;font-weight:600;padding:12px 10px;color:#222}
.cart-badge{position:absolute;right:6px;top:4px;width:13px;height:13px;border-radius:50%;background:#f36b21;color:#fff;font-size:8px;text-align:center;line-height:13px}
.main-nav{left:328px;top:89px;display:flex;gap:0;font-family:"Montserrat",sans-serif;font-size:13px;font-weight:500;color:var(--ink)}
.main-nav span{margin-right:25px}
/* hero */
.hero{left:0;top:120px;width:1200px;height:549px;background:linear-gradient(180deg,#7e99b3 0%,#8aa07a 45%,#5f6b4f 75%,#8a8278 100%)}
.hero-photo{left:0;top:0;width:760px;height:549px;background:radial-gradient(ellipse at 55% 45%,#d8b497 0%,#7a6a5c 45%,transparent 75%)}
.hero h1{left:778px;top:134px;font-family:"Montserrat",sans-serif;font-weight:900;font-size:60px;line-height:56px;color:#fff;letter-spacing:1px}
.hero p{left:787px;top:268px;font-family:"Montserrat",sans-serif;font-weight:700;font-size:20px;line-height:28px;color:#fff}
.btn{background:var(--yellow);color:#111;font-family:"Montserrat",sans-serif;font-weight:800;text-align:center}
.hero .btn{left:787px;top:349px;width:144px;height:47px;line-height:47px;font-size:17px}
.hero-dot{left:949px;top:355px;width:6px;height:6px;border-radius:50%;background:#ddd}
.hero-arrow{top:258px;width:35px;height:34px;background:#fff}
.hero-arrow svg{position:absolute;left:10px;top:9px}
/* categories */
.cat{top:691px;width:244px;height:284px}
.cat-label{position:absolute;bottom:22px;left:18px;font-family:"Montserrat",sans-serif;font-weight:600;font-size:19px;line-height:23px;color:#fff}
.cat-label.chip{background:rgba(255,255,255,.65);color:#111;padding:4px 15px;left:8px;bottom:24px}
/* products */
.section-title{font-family:"Montserrat",sans-serif;font-weight:700;font-size:20px;color:var(--ink)}
.products-title{left:0;width:1200px;top:1022px;text-align:center}
.product{top:1082px;width:223px;height:298px;border:1px solid #c8c8c8;background:#fff}
.product-img{position:absolute;left:20px;top:20px;width:181px;height:175px;border-radius:4px}
.product-name{position:absolute;left:0;right:0;top:233px;text-align:center;font-family:"Montserrat",sans-serif;font-weight:600;font-size:15px;line-height:19px;color:var(--ink)}
.prod-arrow{top:1216px}
/* custom build */
.build-img{left:132px;top:1436px;width:331px;height:387px;background:linear-gradient(135deg,#dedede 0%,#dedede 50%,#8fd17a 50%,#9bd6e0 100%)}
.build-title{left:522px;top:1498px}
.build-copy{left:523px;top:1550px;width:520px;font-size:17.5px;line-height:25.6px;color:#333}
.build .btn{left:525px;top:1708px;width:134px;height:43px;line-height:43px;font-size:16px;color:#fff}
/* reviews */
.reviews{left:0;top:1876px;width:1200px;height:345px;background:var(--band)}
.reviews .section-title{left:130px;top:46px;font-size:21px}
.rev-arrows{left:1034px;top:48px}
.review{top:82px;width:302px;height:218px;background:#fff;padding:26px 30px}
.stars{color:var(--star);font-size:16px;letter-spacing:1px}
.review p{margin-top:14px;font-size:12.3px;line-height:17.6px;color:#333}
.review b{display:block;margin-top:15px;font-family:"Montserrat",sans-serif;font-size:10px;font-weight:700;color:#111}
/* features */
.features{left:0;top:2221px;width:1200px;height:268px;background:var(--blue)}
.feature{top:0;width:366px;text-align:center}
.feature svg{display:block;margin:44px auto 0}
.feature h3{margin-top:21px;font-family:"Montserrat",sans-serif;font-weight:800;font-size:16.5px;color:#fff}
.feature p{margin-top:12px;font-size:13.5px;line-height:17.6px;color:var(--blue-light)}
/* footer */
.site-footer .brand{left:132px;top:2640px;font-size:48px}
.foot-col{top:2536px;font-size:12px;color:#222}
.foot-col h4{font-family:"Montserrat",sans-serif;font-weight:700;font-size:12.5px;margin-bottom:22px;color:#111}
.foot-col li{list-style:none;line-height:19.8px}
.contact-row{display:flex;gap:10px;align-items:flex-start;margin-bottom:18px;line-height:16px}
.ci{width:22px;height:22px;border-radius:50%;background:var(--blue);flex:none;margin-top:5px;position:relative}
.ci svg{position:absolute;left:5px;top:5px}
.divider{left:131px;top:2757px;width:935px;height:1px;background:#ddd}
.copyright{left:0;width:1200px;top:2787px;text-align:center;font-size:9.5px;color:#222}
</style>
</head>
<body>

<header class="site-header">
  <div class="abs brand"><span class="brand-dot"></span>TideRolls</div>
  <div class="abs help">
    <svg width="28" height="28" viewBox="0 0 24 24" fill="none" stroke="#111" stroke-width="1.6"><path d="M5 3h3l2 5-2 1.5a11 11 0 0 0 6.5 6.5L16 14l5 2v3a2 2 0 0 1-2 2A17 17 0 0 1 3 5a2 2 0 0 1 2-2z"/></svg>
    <div><small>NEED HELP?</small><strong>555.014.2290</strong></div>
  </div>
  <div class="abs search">SEARCH
    <svg width="11" height="11" viewBox="0 0 12 12" fill="none" stroke="#666" stroke-width="1.5"><circle cx="5" cy="5" r="3.8"/><path d="M8 8l3 3"/></svg>
  </div>
  <div class="abs cart">MY CART
    <svg class="abs" style="left:60px;top:8px" width="22" height="20" viewBox="0 0 22 20" fill="none" stroke="#333" stroke-width="1.4"><path d="M1 2h3l3 11h11l2-8H6"/><circle cx="9" cy="17" r="1.5"/><circle cx="16" cy="17" r="1.5"/></svg>
    <span class="cart-badge">0</span>
  </div>
  <nav class="abs main-nav">
    <span>CUSTOM TSHIRTS</span><span style="margin-right:32px">POPULAR BRANDS</span><span style="margin-right:32px">POPULAR STYLES</span><span style="margin-right:31px">TEMPLATES</span><span>ACCESSORIES</span><span>SERVICES</span>
  </nav>
</header>

<section class="abs hero">
  <div class="abs hero-photo" role="img" aria-label="Smiling couple wearing printed slogan t-shirts outdoors by a river"></div>
  <h1 class="abs">CUSTOM<br>TSHIRTS</h1>
  <p class="abs">Lorem Ipsum is simply dum<br>my text of the printing.</p>
  <div class="abs btn">SHOP NOW</div>
  <span class="abs hero-dot"></span>
  <div class="abs hero-arrow" style="left:0"><svg width="14" height="16" viewBox="0 0 14 16" fill="none" stroke="#111" stroke-width="2.2"><path d="M10 2L4 8l6 6"/></svg></div>
  <div class="abs hero-arrow" style="left:1165px"><svg width="14" height="16" viewBox="0 0 14 16" fill="none" stroke="#111" stroke-width="2.2"><path d="M4 2l6 6-6 6"/></svg></div>
</section>

<section class="categories">
  <div class="abs cat" style="left:88px;background:linear-gradient(160deg,#8d8a7c,#e9e6e2 55%,#5d7a3e)" role="img" aria-label="Woman wearing a white printed t-shirt"><span class="cat-label">Women<br>Tshirts</span></div>
  <div class="abs cat" style="left:345px;background:linear-gradient(160deg,#5f6a70,#b8c9d6 55%,#3c3c3c)" role="img" aria-label="Man in a light blue t-shirt holding a skateboard"><span class="cat-label">Men<br>Tshirts</span></div>
  <div class="abs cat" style="left:601px;background:linear-gradient(90deg,#e4e4e4 0%,#e4e4e4 30%,#2a2a2a 45%,#1e1e1e 100%)" role="img" aria-label="Black zip hoodie with a printed chest design"><span class="cat-label chip">Hoodies</span></div>
  <div class="abs cat" style="left:857px;background:linear-gradient(160deg,#e8e8e8,#f5f5f5 50%,#d9d9d9)" role="img" aria-label="Man in a white polo shirt holding a tablet"><span class="cat-label chip">Polos</span></div>
</section>

<section class="products">
  <h2 class="abs section-title products-title">OUR PRODUCTS</h2>
  <svg class="abs prod-arrow" style="left:88px" width="12" height="20" viewBox="0 0 12 20" fill="none" stroke="#888" stroke-width="2"><path d="M10 2L2 10l8 8"/></svg>
  <div class="abs product" style="left:132px"><div class="product-img" role="img" aria-label="Navy t-shirt with a printed chest label" style="background:radial-gradient(circle at 50% 50%,#2f4c86 0%,#2f4c86 55%,#fff 72%)"></div><div class="product-name">Lorem Ipsum is<br>simply dum</div></div>
  <div class="abs product" style="left:372px"><div class="product-img" role="img" aria-label="Navy polo shirt" style="background:radial-gradient(circle at 50% 50%,#1d3a5c 0%,#1d3a5c 55%,#fff 72%)"></div><div class="product-name">Lorem Ipsum is<br>simply dum</div></div>
  <div class="abs product" style="left:610px"><div class="product-img" role="img" aria-label="Grey t-shirt with logo placeholder" style="background:radial-gradient(circle at 50% 50%,#7e7e7e 0%,#7e7e7e 55%,#fff 72%)"></div><div class="product-name">Lorem Ipsum is<br>simply dum</div></div>
  <div class="abs product" style="left:846px"><div class="product-img" role="img" aria-label="Dark navy t-shirt with design placeholder" style="background:radial-gradient(circle at 50% 50%,#1f2338 0%,#1f2338 55%,#fff 72%)"></div><div class="product-name">Lorem Ipsum is<br>simply dum</div></div>
  <svg class="abs prod-arrow" style="left:1092px" width="12" height="20" viewBox="0 0 12 20" fill="none" stroke="#888" stroke-width="2"><path d="M2 2l8 8-8 8"/></svg>
</section>

<section class="build">
  <div class="abs build-img" role="img" aria-label="Young man wearing a custom printed t-shirt"></div>
  <h2 class="abs section-title build-title">CUSTOM BUILD A SHIRT DESIGN</h2>
  <p class="abs build-copy">Lorem ipsum dolor sit amet, consectetur adipiscing elit, sed do eiusmod tempor incididunt ut labore et dolore magna aliqua. Ut enim ad minim veniam, quis nostrud exercitation ullamco laboris nisi ut aliquip ex ea commodo consequat. Duis aute irure dolor in reprehenderit in voluptate .</p>
  <div class="abs btn">SHOP NOW</div>
</section>

<section class="abs reviews">
  <h2 class="abs section-title">REVIEWS</h2>
  <svg class="abs rev-arrows" width="36" height="16" viewBox="0 0 36 16" fill="none" stroke="#888" stroke-width="1.8"><path d="M8 2L2 8l6 6M28 2l6 6-6 6"/></svg>
  <article class="abs review" style="left:131px"><div class="stars">★★★★★</div><p>Lorem ipsum dolor sit amet, consectetur adipiscing elit, sed do eiusmod tempor incididunt ut labore et dolore magna aliqua. Ut enim ad minim veniam, quis nostrud exercitation ullamco laboris nisi ut aliquip ex ea commodo.</p><b>DANA</b></article>
  <article class="abs review" style="left:447px"><div class="stars">★★★★★</div><p>Lorem ipsum dolor sit amet, consectetur adipiscing elit, sed do eiusmod tempor incididunt ut labore et dolore magna aliqua. Ut enim ad minim veniam, quis nostrud exercitation ullamco laboris nisi ut aliquip ex ea commodo.</p><b>DANA</b></article>
  <article class="abs review" style="left:766px"><div class="stars">★★★★★</div><p>Lorem ipsum dolor sit amet, consectetur adipiscing elit, sed do eiusmod tempor incididunt ut labore et dolore magna aliqua. Ut enim ad minim veniam, quis nostrud exercitation ullamco laboris nisi ut aliquip ex ea commodo.</p><b>DANA</b></article>
</section>

<section class="abs features">
  <div class="abs feature" style="left:49px">
    <svg width="80" height="58" viewBox="0 0 80 58" fill="#fff"><rect x="2" y="2" width="46" height="30" rx="3"/><path d="M50 12h16l12 14v14H50z"/><rect x="2" y="34" width="76" height="8"/><circle cx="20" cy="46" r="9" stroke="#1a9be8" stroke-width="3"/><circle cx="62" cy="46" r="9" stroke="#1a9be8" stroke-width="3"/><text x="25" y="23" text-anchor="middle" font-family="Montserrat,sans-serif" font-weight="800" font-size="13" fill="#1a9be8">FREE</text></svg>
    <h3>FAST FREE DELIVERY</h3>
    <p>Lorem ipsum dolor sit amet,<br>consectetur adipiscing elit, sed do<br>eiusmod tempor incididunt.</p>
  </div>
  <div class="abs feature" style="left:415px">
    <svg width="66" height="62" viewBox="0 0 66 62" fill="#fff"><circle cx="40" cy="20" r="18"/><text x="40" y="28" text-anchor="middle" font-family="Montserrat,sans-serif" font-weight="800" font-size="22" fill="#1a9be8">$</text><path d="M2 42h8v18H2zM12 44c8-4 14-4 22 0h8c4 0 4 6 0 6H28h16l14-8c5-2 7 3 3 6L44 58H12z"/></svg>
    <h3>BETTER PRICING</h3>
    <p>Lorem ipsum dolor sit amet,<br>consectetur adipiscing elit, sed do<br>eiusmod tempor incididunt.</p>
  </div>
  <div class="abs feature" style="left:776px">
    <svg width="62" height="62" viewBox="0 0 62 62" fill="#fff"><path d="M44 4l14 14-34 34H10V38z"/><path d="M6 6l12 12-6 6L0 12zM40 40l12 12-6 6-12-12z"/></svg>
    <h3>DESIGN REVIEW &amp; REPAIR</h3>
    <p>Lorem ipsum dolor sit amet,<br>consectetur adipiscing elit, sed do<br>eiusmod tempor incididunt.</p>
  </div>
</section>

<footer class="site-footer">
  <div class="abs brand"><span class="brand-dot" style="width:30px;height:30px"></span>TideRolls</div>
  <div class="abs foot-col" style="left:469px"><h4>MENU</h4><ul><li>CUSTOM SHIRTS</li><li>POPULAR BRANDS</li><li>POPULAR STYLES</li><li>TEMPLATES</li><li>ACCESSORIES</li><li>SERVICES</li></ul></div>
  <div class="abs foot-col" style="left:698px"><h4>CONTACT US</h4>
    <div class="contact-row"><span class="ci"><svg width="12" height="12" viewBox="0 0 12 12" fill="#fff"><path d="M6 0a4 4 0 0 1 4 4c0 3-4 8-4 8S2 7 2 4a4 4 0 0 1 4-4z"/></svg></span><span>2150 Harbor Lane<br>Alder, CA 90000</span></div>
    <div class="contact-row"><span class="ci"><svg width="12" height="12" viewBox="0 0 24 24" fill="#fff"><path d="M5 3h4l2 5-3 2a11 11 0 0 0 6 6l2-3 5 2v4a2 2 0 0 1-2 2A17 17 0 0 1 3 5a2 2 0 0 1 2-2z"/></svg></span><span>Call Us<br>555.014.2290</span></div>
    <div class="contact-row"><span class="ci"><svg width="12" height="12" viewBox="0 0 12 12" fill="#fff"><rect x="0" y="2" width="12" height="8" rx="1"/><path d="M0 2l6 5 6-5" stroke="#1a9be8" fill="none"/></svg></span><span>E mail Us<br>info@tiderolls.com</span></div>
  </div>
  <div class="abs foot-col" style="left:960px"><h4>FOLLOW US</h4>
    <div class="contact-row"><span class="ci"></span><span>Like us on<br>PALMNEST</span></div>
    <div class="contact-row"><span class="ci"></span><span>Follow us on<br>CHIRPLO</span></div>
    <div class="contact-row"><span class="ci"></span><span>Follow us on<br>LINKORA</span></div>
  </div>
  <div class="abs divider"></div>
  <p class="abs copyright">Copyright © 2021 All Rights Reserved</p>
</footer>

</body>
</html>
```